Doctors clinic requires stationary designed

We require various types of stationary to be design based on the logo (attached). We require the following:
- Letterhead (A4 Portrait)
- Business Card (must include UV spot on rear)
- With compliments slip (DL Landscape)
- Appointments card (Folded A6)

We are a young clinical practice which boasts a modern and sophisticated approach to medicine so we require something which feels fresh and modern. Please include colours represented in the logo (contrasting teal and grey). We are calling for creative minds to put forth their ideas and we will be actively providing feedback on all designs.

thank you

```html
<!DOCTYPE html>
<html lang="en">
<head>
<meta charset="utf-8">
<title>Dr Clara Whitfield – Business Card</title>
<link href="https://fonts.googleapis.com/css2?family=Open+Sans:wght@400;600&family=Noto+Serif:wght@700&display=swap" rel="stylesheet">
<style>
  :root {
    --bg: #e9eceb;
    --white: #ffffff;
    --teal: #14998f;
    --teal-dark: #0d7c75;
    --teal-light: #4cbcae;
    --ink-on-teal: #ffffff;
  }
  * { box-sizing: border-box; margin: 0; padding: 0; }
  html, body { width: 1200px; height: 1000px; overflow: hidden; }
  body {
    background: var(--bg);
    font-family: "Open Sans", Arial, sans-serif;
    position: relative;
  }
  .card {
    position: absolute;
    left: 250px;
    width: 700px;
    height: 400px;
    overflow: hidden;
    box-shadow: 0 8px 24px rgba(0,0,0,0.18);
  }
  .card--front { top: 70px; background: var(--white); }
  .card--back {
    top: 530px;
    background: linear-gradient(160deg, var(--teal-dark) 0%, var(--teal) 45%, var(--teal-light) 75%, var(--teal) 100%);
  }

  /* Front – identity side */
  .identity {
    position: absolute;
    left: 0; top: 0;
    width: 380px; height: 400px;
    display: flex;
    flex-direction: column;
    align-items: center;
    justify-content: center;
    gap: 10px;
    color: var(--teal);
  }
  .identity__mark {
    width: 56px; height: 56px;
    border: 3px solid var(--teal);
    border-radius: 50%;
    margin-bottom: 8px;
  }
  .identity__name {
    font-size: 30px;
    font-weight: 600;
    letter-spacing: -0.3px;
    line-height: 1;
  }
  .identity__specialty {
    font-size: 17px;
    font-weight: 600;
    line-height: 1;
  }

  /* Front – contact panel */
  .contact-panel {
    position: absolute;
    left: 380px; top: 0;
    width: 320px; height: 400px;
    background: linear-gradient(165deg, var(--teal-dark) 0%, var(--teal) 40%, var(--teal-light) 80%, var(--teal) 100%);
    color: var(--ink-on-teal);
    padding: 82px 24px 0 44px;
  }
  .contact-panel__name {
    font-family: "Noto Serif", Georgia, serif;
    font-weight: 700;
    font-size: 16px;
    line-height: 1.2;
  }
  .contact-panel__role { font-size: 12px; margin-top: 1px; }
  .contact-panel__rule {
    border: 0;
    border-top: 1px solid rgba(255,255,255,0.75);
    margin: 10px 0 14px;
    width: 240px;
  }
  .contact-list { list-style: none; font-size: 13.5px; line-height: 1.35; }
  .contact-item {
    position: relative;
    margin-bottom: 13px;
  }

  /* Icon tab attached to each contact line */
  .icon-tab {
    position: absolute;
    left: -44px;
    top: -3px;
    width: 30px; height: 24px;
    background: var(--white);
    border-radius: 0 12px 12px 0;
    display: flex;
    align-items: center;
    justify-content: center;
    padding-right: 4px;
  }
  .icon-tab svg { width: 13px; height: 13px; fill: var(--teal); }

  /* Back */
  .card--back .gloss {
    position: absolute; inset: 0;
    background: linear-gradient(180deg, rgba(255,255,255,0.18) 0%, rgba(255,255,255,0) 40%);
  }
  .uv-spot {
    position: absolute;
    left: 50%; top: 50%;
    transform: translate(-50%, -50%);
    display: flex;
    flex-direction: column;
    align-items: center;
    gap: 14px;
    color: rgba(255,255,255,0.9);
  }
  .uv-spot__mark {
    width: 150px; height: 150px;
    border: 6px solid rgba(255,255,255,0.85);
    border-radius: 50%;
  }
  .uv-spot__name { font-size: 26px; font-weight: 600; white-space: nowrap; }
</style>
</head>
<body>

<section class="card card--front">
  <div class="identity">
    <span class="identity__mark" aria-hidden="true"></span>
    <span class="identity__name">Dr Clara Whitfield</span>
    <span class="identity__specialty">Obstetrician and Gynaecologist</span>
  </div>

  <div class="contact-panel">
    <p class="contact-panel__name">Lena Marsh</p>
    <p class="contact-panel__role">Graphic Designer</p>
    <hr class="contact-panel__rule">
    <ul class="contact-list">
      <li class="contact-item">
        <span class="icon-tab" aria-label="Address">
          <svg viewBox="0 0 24 24"><path d="M12 2a7 7 0 0 0-7 7c0 5 7 13 7 13s7-8 7-13a7 7 0 0 0-7-7zm0 9.5A2.5 2.5 0 1 1 12 6.5a2.5 2.5 0 0 1 0 5z"/></svg>
        </span>
        your address, city and pincode<br>country
      </li>
      <li class="contact-item">
        <span class="icon-tab" aria-label="Phone">
          <svg viewBox="0 0 24 24"><path d="M6.6 10.8a15 15 0 0 0 6.6 6.6l2.2-2.2a1 1 0 0 1 1-.25 11.4 11.4 0 0 0 3.6.57 1 1 0 0 1 1 1V20a1 1 0 0 1-1 1A17 17 0 0 1 3 4a1 1 0 0 1 1-1h3.5a1 1 0 0 1 1 1c0 1.25.2 2.45.57 3.6a1 1 0 0 1-.25 1z"/></svg>
        </span>
        (002) 4410 2278
      </li>
      <li class="contact-item">
        <span class="icon-tab" aria-label="Fax">
          <svg viewBox="0 0 24 24"><path d="M7 2h8l3 3v5H7zM4 11h16a2 2 0 0 1 2 2v7a2 2 0 0 1-2 2H4a2 2 0 0 1-2-2v-7a2 2 0 0 1 2-2zm3 3v2h3v-2zm5 0v2h5v-2zm-5 4v2h10v-2z"/></svg>
        </span>
        (001) 3030 918273
      </li>
      <li class="contact-item">
        <span class="icon-tab" aria-label="Website">
          <svg viewBox="0 0 24 24"><path d="M12 2a10 10 0 1 0 0 20 10 10 0 0 0 0-20zm6.9 6h-2.9a15 15 0 0 0-1.4-3.6A8 8 0 0 1 18.9 8zM12 4c.8 1.2 1.5 2.5 1.9 4h-3.8c.4-1.5 1.1-2.8 1.9-4zM4.3 14a8 8 0 0 1 0-4h3.4a16 16 0 0 0 0 4zm.8 2h2.9c.3 1.3.8 2.5 1.4 3.6A8 8 0 0 1 5.1 16zM8 8H5.1a8 8 0 0 1 4.3-3.6C8.8 5.5 8.3 6.7 8 8zm4 12c-.8-1.2-1.5-2.5-1.9-4h3.8c-.4 1.5-1.1 2.8-1.9 4zm2.3-6H9.7a14 14 0 0 1 0-4h4.6a14 14 0 0 1 0 4zm.3 5.6c.6-1.1 1.1-2.3 1.4-3.6h2.9a8 8 0 0 1-4.3 3.6zm1.7-5.6a16 16 0 0 0 0-4h3.4a8 8 0 0 1 0 4z"/></svg>
        </span>
        www.whitfieldclinic.com
      </li>
    </ul>
  </div>
</section>

<section class="card card--back">
  <div class="gloss" aria-hidden="true"></div>
  <div class="uv-spot">
    <span class="uv-spot__mark" aria-hidden="true"></span>
    <span class="uv-spot__name">Dr Clara Whitfield</span>
  </div>
</section>

</body>
</html>
```